" Assessoria e consultoria de projetos agropecuários com foco em bovinos. DIFERENCIAIS ? Atendimento personalizado; ? Foco em processos; Melhoria continua - metodologia LEAN ? Foco no cliente e na qualidade do serviço; ? Acompanhamento dos resultados gerados pela consultoria; ? Serviço com conhecimento agregado. Atendimento personalizado: A Brota enxerga a necessidade do contato personalizado com o cliente, demonstrando constantemente que a empresa está interessada em ajudá-lo e trazer soluções para seus problemas. ? Foco em processos: Como a maioria das empresas que prestam consultoria na área estão mais voltadas para TÉCNICAS animal, o foco em processos e gestao por processos torna-se um diferencial da Brota. A empresa poderia aproveitar essa vantagem divulgando a importância do gerenciamento eficaz nas fazendas através dos processos agropecuários. ? Foco no cliente e na qualidade do serviço: Através do atendimento personalizado, o consultor da Brota tem a responsabilidade de manter o comprometimento com o cliente e com a qualidade dos serviços entregues. Assim, a empresa cria uma boa relação com os consumidores, fidelizando-os. ? Acompanhamento dos resultados gerados pela consultoria: Além de prestar consultoria, a Empresa auxilia o cliente a implementar as técnicas e soluções, fazendo o acompanhamento de resultados com indicadores. ? Serviço com maior valor agregado: Através da constante busca por conhecimento na área, a qualidade dos projetos entregues será cada vez maior, consequentemente tornando-os mais eficazes e eficientes. "

```html
<!DOCTYPE html>
<html lang="en">
<head>
<meta charset="utf-8">
<title>Brota Letterhead</title>
<link rel="stylesheet" href="https://fonts.googleapis.com/css2?family=Montserrat:wght@600&family=Open+Sans:wght@400;600&display=swap">
<style>
  :root {
    --backdrop: #e9ebee;
    --paper: #ffffff;
    --navy: #1c2b4d;
    --green: #2f8a3f;
    --ink: #4a4f57;
    --muted: #8a9099;
    --sign-fill: #e3e6ea;
  }
  * { box-sizing: border-box; margin: 0; padding: 0; }
  html, body {
    width: 1200px; height: 1200px; overflow: hidden;
    background: var(--backdrop);
  }
  .letterhead {
    position: absolute; left: 211px; top: 50px;
    width: 778px; height: 1100px;
    background: var(--paper);
    box-shadow: 0 6px 24px rgba(0,0,0,0.12);
    font-family: "Open Sans", Arial, sans-serif;
    color: var(--ink);
    overflow: hidden;
  }
  .brand {
    position: absolute; top: 56px; right: 70px;
    display: flex; align-items: center; gap: 12px;
  }
  .brand-dot {
    width: 22px; height: 22px; border-radius: 50%;
    background: var(--green);
  }
  .brand-name {
    font-family: "Montserrat", Arial, sans-serif;
    font-weight: 600; font-size: 34px; letter-spacing: 4px;
    color: var(--green);
  }
  .letter-body {
    position: absolute; left: 70px; right: 70px; top: 150px;
    font-size: 13.5px; line-height: 1.75;
  }
  .salutation { font-weight: 600; color: var(--navy); margin-bottom: 22px; font-size: 15px; }
  .letter-body p { margin-bottom: 18px; text-align: justify; }
  .contact-list {
    position: absolute; left: 70px; top: 650px;
    list-style: none; font-size: 12px; color: var(--muted);
  }
  .contact-list li { display: flex; align-items: center; gap: 10px; margin-bottom: 10px; }
  .contact-icon {
    width: 20px; height: 20px; border-radius: 50%;
    background: var(--green); display: flex; align-items: center; justify-content: center;
  }
  .closing { position: absolute; left: 70px; top: 800px; font-size: 13px; }
  .signature {
    width: 170px; height: 54px; margin: 14px 0 8px;
    background: var(--sign-fill); border-radius: 4px;
  }
  .signer-name { font-weight: 600; color: var(--navy); }
  .signer-role { color: var(--muted); font-size: 12px; }
  .footer-rule {
    position: absolute; left: 0; right: 0; bottom: 0;
    height: 10px; background: var(--green);
  }
</style>
</head>
<body>
  <main class="letterhead">
    <header class="brand">
      <span class="brand-dot"></span>
      <span class="brand-name">BROTA</span>
    </header>

    <section class="letter-body">
      <p class="salutation">Dear Mr. Alvarez</p>
      <p>Thank you for meeting with our team last week to discuss the future of your cattle operation. We have reviewed the notes from the farm visit and prepared a plan focused on clear processes, steady follow-up and measurable results for every stage of the herd cycle.</p>
      <p>Our consultants will work beside your staff to map daily routines, remove waste and set simple indicators for feed, weight gain and health. Each month we will share a short report and meet with you to adjust the plan as the season changes.</p>
      <p>During the first phase we will visit the property twice, interview the team and review the records you already keep. This will give us a clear starting point and help us agree on the goals that matter most to you.</p>
      <p>We look forward to growing with you and to building a long and trusted partnership.</p>
    </section>

    <ul class="contact-list">
      <li>
        <span class="contact-icon">
          <svg width="11" height="11" viewBox="0 0 24 24"><path fill="#fff" d="M6.6 10.8a15 15 0 0 0 6.6 6.6l2.2-2.2a1 1 0 0 1 1-.25 11.4 11.4 0 0 0 3.6.57 1 1 0 0 1 1 1V20a1 1 0 0 1-1 1A17 17 0 0 1 3 4a1 1 0 0 1 1-1h3.5a1 1 0 0 1 1 1c0 1.25.2 2.45.57 3.6a1 1 0 0 1-.25 1z"/></svg>
        </span>(55) 3400-1200
      </li>
      <li>
        <span class="contact-icon">
          <svg width="11" height="11" viewBox="0 0 24 24"><path fill="#fff" d="M2 5h20v14H2zM3.5 6.5 12 13l8.5-6.5" stroke="#2f8a3f" stroke-width="1.6"/></svg>
        </span>contato@brota.com.br
      </li>
      <li>
        <span class="contact-icon">
          <svg width="11" height="11" viewBox="0 0 24 24"><path fill="#fff" d="M12 2a7 7 0 0 0-7 7c0 5 7 13 7 13s7-8 7-13a7 7 0 0 0-7-7zm0 9.5A2.5 2.5 0 1 1 12 6.5a2.5 2.5 0 0 1 0 5z"/></svg>
        </span>Rua das Palmeiras, 120
      </li>
    </ul>

    <section class="closing">
      <p>Yours sincerely,</p>
      <div class="signature" role="img" aria-label="Handwritten signature of Rafael Costa"></div>
      <p class="signer-name">Rafael Costa</p>
      <p class="signer-role">Lead Consultant</p>
    </section>

    <div class="footer-rule" aria-hidden="true"></div>
  </main>
</body>
</html>
```